Easy Business Card / Presentation Cover Design Project

We are looking for a business card design, covers for powerpoint presentations for investors, and possibly simple stationary for a Chicago real estate development firm. Our new logo is attached below.

We rehab and provide newly constructed homes. We are not a real estate brokerage firm (i.e., agents such as Meridale 47) and only operate in the Chicago area.

In terms of design, sophisticated and high end that would appeal to investors (theme should resemble investment banks, hedge funds, private equity rather than tech startup).

Target Market(s)

Investors, banks, financing sources

Industry/Entity Type

Real Estate

Requirements
Must have
• Two deliverables here. 1) Business card 2) Covers for powerpoint presentation.

Must be able to look sophisticated and high end when printed. Please think through the type of printing that will be needed. Would prefer something that can be printed in raised ink but digital is ok as well.

Will be printed on heavy paper.

Business Card: Horizontal Layout, no black backgrounds,

For presentation front cover, should include logo only. For back cover, should include contact info. Horizontal and should not contain any information that will need to be changed (i.e. date or client name)
Nice to have
• Would like to have the edges colored but not required. Please show multiple designs
Should not have
• Should not have any die cut or embossed type of designs. Shape should be standard size.

We are not a design firm, a retail firm, or a consumer product firm.

Please do not incorporate a house, buildings, etc. This must be very professional looking.

```html
<!DOCTYPE html>
<html lang="en">
<head>
<meta charset="utf-8">
<title>KVR Realty — Business Card</title>
<link href="https://fonts.googleapis.com/css2?family=Cinzel:wght@400&display=swap" rel="stylesheet">
<style>
  :root {
    --backdrop: #ece9e4;
    --card: #ffffff;
    --ink: #55565a;
    --ink-soft: #6a6b70;
    --brand-blue: #1f8ff0;
    --brand-blue-light: #5bb4ff;
    --brand-grey: #8c8d91;
    --divider: #b9babd;
  }
  * { box-sizing: border-box; margin: 0; padding: 0; }
  html, body { width: 1200px; height: 1200px; overflow: hidden; }
  body {
    background: var(--backdrop);
    font-family: "Cinzel", "Trajan Pro", Georgia, serif;
    color: var(--ink);
    display: flex;
    flex-direction: column;
    align-items: center;
    justify-content: center;
    gap: 70px;
  }
  .card {
    position: relative;
    width: 860px;
    height: 491px;
    background: var(--card);
    box-shadow: 0 10px 28px rgba(0,0,0,0.18);
    overflow: hidden;
  }

  /* Back side: name + contact details */
  .card--back .edge-right {
    position: absolute; top: 0; right: 0;
    width: 10px; height: 100%;
    background: var(--brand-blue);
  }
  .card--back .corner-wedge {
    position: absolute; left: 0; bottom: 0;
    width: 190px; height: 40px;
  }
  .card--back .divider {
    position: absolute;
    left: 292px; top: 40px; bottom: 40px;
    border-left: 2px dashed var(--divider);
  }
  .holder-name {
    position: absolute;
    left: 0; width: 292px;
    top: 50%; transform: translateY(-50%);
    text-align: center;
    font-size: 30px;
    letter-spacing: 1px;
    color: var(--ink);
  }
  .contact {
    position: absolute;
    left: 335px; top: 84px;
    font-size: 19px;
    line-height: 1.35;
    letter-spacing: 0.5px;
    color: var(--ink-soft);
    list-style: none;
  }
  .contact .address { margin-top: 26px; }

  /* Front side: brand name over ring pattern area */
  .card--front .ring-pattern {
    position: absolute; inset: 0;
    background:
      radial-gradient(ellipse 34% 40% at 50% 50%, #ffffff 0 70%, rgba(255,255,255,0) 100%),
      radial-gradient(ellipse 70% 85% at 50% 50%, var(--brand-blue-light) 0%, var(--brand-blue) 45%, var(--brand-grey) 75%, #ffffff 100%);
  }
  .brand {
    position: absolute; inset: 0;
    display: flex; flex-direction: column;
    align-items: center; justify-content: center;
    color: var(--ink);
    font-weight: 400;
    line-height: 0.95;
  }
  .brand .brand-main { font-size: 104px; letter-spacing: 2px; }
  .brand .brand-sub { font-size: 54px; letter-spacing: 3px; }
</style>
</head>
<body>

  <section class="card card--back" aria-label="Business card back">
    <div class="edge-right"></div>
    <svg class="corner-wedge" viewBox="0 0 190 40" aria-hidden="true">
      <polygon points="0,40 0,8 190,40" fill="var(--brand-blue)"/>
    </svg>
    <div class="divider"></div>
    <p class="holder-name">Daniel Hale</p>
    <ul class="contact">
      <li>(01) 5550 4127</li>
      <li>daniel@kvrrealty.com</li>
      <li class="address">48 Harbor Lane,</li>
      <li>Chicago,</li>
      <li>USA</li>
    </ul>
  </section>

  <section class="card card--front" aria-label="Business card front">
    <div class="ring-pattern" role="img" aria-label="Interlocking blue and grey ring pattern framing the brand name"></div>
    <div class="brand">
      <span class="brand-main">KVR</span>
      <span class="brand-sub">Realty</span>
    </div>
  </section>

</body>
</html>
```